Update cover page from corporate ppt template

We would like you to design a new cover page for our corporate presentation template

Attached you will find our existing template with the previous cover pages used in the past years.

As you can see, we have used transparency lines in different directions and also tried to develop a new design with mosaic/squares but we are not entirely satisfied (logo lost in the sky, ...)

You can reuse the same picture (mountain with the bridge, i.e not the one of the last cover page)

Feel free to come up with new ideas

```html
<!DOCTYPE html>
<html lang="en">
<head>
<meta charset="utf-8">
<title>Board of Directors – Cover Page Options</title>
<link href="https://fonts.googleapis.com/css2?family=Montserrat:wght@300;400&display=swap" rel="stylesheet">
<style>
  :root {
    --navy: #172040;
    --white: #ffffff;
    --gold: #b89a78;
    --brand-grey: #6f7280;
    --brand-grey-light: #9aa0b4;
    --arc-blue: #7b8fcf;
    --arc-light: #dfe6f5;
    --sky: #5f9de0;
    --rock: #3e5673;
    --forest: #4a5a2a;
    --larch: #c9a436;
    --lake: #7fcfc0;
    --stone: #4b5968;
    --sand: #b8ae86;
    --pine: #2e3a2c;
  }
  * { margin: 0; padding: 0; box-sizing: border-box; }
  html, body { width: 1200px; height: 2194px; overflow: hidden; background: var(--white); }
  body { position: relative; font-family: "Montserrat", sans-serif; }

  .slide {
    position: absolute; width: 450px; height: 338px; overflow: hidden;
    box-shadow: 6px 8px 18px rgba(0,0,0,0.28);
  }
  .slide--light { background: var(--white); color: var(--navy); }
  .slide--dark { background: var(--navy); color: var(--white); }
  .col-left { left: 92px; }
  .col-right { left: 654px; }
  .row-1 { top: 157px; } .row-2 { top: 542px; } .row-3 { top: 926px; }
  .row-4 { top: 1310px; } .row-5 { top: 1694px; }

  .slide svg.art { position: absolute; inset: 0; width: 450px; height: 338px; }

  .brand {
    position: absolute; font-weight: 400; font-size: 25px; letter-spacing: 1px;
    color: var(--brand-grey); line-height: 1;
  }
  .slide--dark .brand { color: var(--brand-grey-light); }
  .title { position: absolute; font-weight: 400; line-height: 1.1; }
  .date { position: absolute; font-weight: 400; color: var(--gold); }
  .slide--dark .date { color: #d8d2c4; }

  /* chevron layout, stacked title */
  .chev-stack .brand { left: 50px; top: 90px; }
  .chev-stack .title { left: 42px; top: 133px; font-size: 29px; }
  .chev-stack .date { left: 63px; top: 210px; font-size: 14px; }
  /* chevron layout, single-line title */
  .chev-line .brand { left: 47px; top: 108px; }
  .chev-line .title { left: 42px; top: 155px; font-size: 22px; }
  .chev-line .date { left: 42px; top: 189px; font-size: 12px; }

  /* mosaic */
  .mosaic .brand { left: 37px; top: 90px; }
  .mosaic .title { left: 36px; top: 134px; font-size: 29px; }
  .mosaic .date { left: 36px; top: 211px; font-size: 14px; }
  .tile { position: absolute; }

  /* panorama with arc band */
  .pano .title { left: 36px; top: 255px; font-size: 26px; }
  .pano .date { left: 39px; top: 288px; font-size: 12px; }
  .pano .brand { left: 305px; top: 263px; }
</style>
</head>
<body>

<!-- Chevron, stacked title, light -->
<section class="slide slide--light chev-stack col-left row-1">
  <svg class="art" viewBox="0 0 450 338">
    <defs>
      <linearGradient id="mtnA" x1="0" y1="0" x2="0.3" y2="1">
        <stop offset="0" stop-color="#6aa8e8"/><stop offset="0.45" stop-color="#3e5673"/>
        <stop offset="0.75" stop-color="#4a5a2a"/><stop offset="1" stop-color="#c9a436"/>
      </linearGradient>
    </defs>
    <polygon points="240,0 265,0 381,169 265,338 240,338 356,169" fill="#d9e7f5" opacity="0.7"/>
    <polygon points="418,0 437,0 450,19 450,40" fill="#d9e7f5" opacity="0.7"/>
    <polygon role="img" aria-label="Photo: alpine mountain with suspension bridge over autumn larch forest" points="259,0 437,0 450,19 450,319 437,338 259,338 375,169" fill="url(#mtnA)"/>
  </svg>
  <div class="brand">BREVANI</div>
  <h1 class="title">Board of<br>Directors</h1>
  <p class="date">May 2024</p>
</section>

<!-- Chevron, stacked title, dark -->
<section class="slide slide--dark chev-stack col-right row-1">
  <svg class="art" viewBox="0 0 450 338">
    <polygon points="140,0 150,0 266,169 150,338 140,338 256,169" fill="#ffffff" opacity="0.9"/>
    <polygon points="345,0 355,0 450,138 450,152" fill="#ffffff" opacity="0.9"/>
    <polygon role="img" aria-label="Photo: alpine mountain with suspension bridge over autumn larch forest" points="259,0 450,0 450,0 450,338 259,338 375,169" fill="url(#mtnA)"/>
    <polygon points="340,0 450,0 450,160" fill="#d9e7f5" opacity="0.35"/>
    <polygon points="440,0 450,0 450,14" fill="#ffffff" opacity="0.9"/>
    <polygon points="340,338 450,338 450,178" fill="#172040"/>
    <polygon points="340,0 450,0 450,160" fill="#172040"/>
    <polygon points="330,0 345,0 450,152 450,174" fill="#ffffff" opacity="0.9"/>
    <polygon points="330,338 345,338 450,186 450,164" fill="#ffffff" opacity="0.9"/>
  </svg>
  <div class="brand">BREVANI</div>
  <h1 class="title">Board of<br>Directors</h1>
  <p class="date">May 2024</p>
</section>

<!-- Chevron, single line, dark -->
<section class="slide slide--dark chev-line col-left row-2">
  <svg class="art" viewBox="0 0 450 338">
    <polygon points="140,0 150,0 266,169 150,338 140,338 256,169" fill="#ffffff" opacity="0.9"/>
    <polygon role="img" aria-label="Photo: alpine mountain with suspension bridge over autumn larch forest" points="150,0 450,0 450,338 150,338 266,169" fill="url(#mtnA)"/>
    <polygon points="355,0 450,0 450,138" fill="#172040"/>
    <polygon points="355,338 450,338 450,200" fill="#172040"/>
    <polygon points="345,0 358,0 450,134 450,152" fill="#ffffff" opacity="0.9"/>
    <polygon points="345,338 358,338 450,204 450,186" fill="#ffffff" opacity="0.9"/>
  </svg>
  <div class="brand">BREVANI</div>
  <h1 class="title">Board of Directors</h1>
  <p class="date">May 2024</p>
</section>

<!-- Chevron, single line, light -->
<section class="slide slide--light chev-line col-right row-2">
  <svg class="art" viewBox="0 0 450 338">
    <polygon points="140,0 158,0 274,169 158,338 140,338 256,169" fill="#d9e7f5" opacity="0.7"/>
    <polygon role="img" aria-label="Photo: alpine mountain with suspension bridge over autumn larch forest" points="158,0 450,0 450,338 158,338 274,169" fill="url(#mtnA)"/>
    <polygon points="355,0 450,0 450,138" fill="#ffffff"/>
    <polygon points="355,338 450,338 450,200" fill="#ffffff"/>
    <polygon points="345,0 360,0 450,131 450,152" fill="#d9e7f5" opacity="0.8"/>
    <polygon points="345,338 360,338 450,207 450,186" fill="#d9e7f5" opacity="0.8"/>
  </svg>
  <div class="brand">BREVANI</div>
  <h1 class="title">Board of Directors</h1>
  <p class="date">May 2024</p>
</section>

<!-- Mosaic, light -->
<section class="slide slide--light mosaic col-left row-3">
  <div class="tile" role="img" aria-label="Photo tile: dark pine forest" style="left:207px;top:8px;width:77px;height:76px;background:linear-gradient(#2e3a2c,#3a4630)"></div>
  <div class="tile" role="img" aria-label="Photo tile: golden forest canopy" style="left:207px;top:88px;width:77px;height:76px;background:linear-gradient(#8d7d4f,#6f6640)"></div>
  <div class="tile" role="img" aria-label="Photo tile: forest with winding road" style="left:207px;top:169px;width:77px;height:98px;background:linear-gradient(#4a5a2a,#6a7a3a)"></div>
  <div class="tile" role="img" aria-label="Photo tile: road winding beside a turquoise lake" style="left:287px;top:8px;width:76px;height:259px;background:linear-gradient(#4a5a2a,#5d7a3a 55%,#7fcfc0)"></div>
  <div class="tile" role="img" aria-label="Photo tile: pale lake water" style="left:367px;top:8px;width:77px;height:97px;background:linear-gradient(#eef6f4,#cfeae5)"></div>
  <div class="tile" style="left:367px;top:109px;width:77px;height:76px;background:#b9e3dc"></div>
  <div class="tile" style="left:367px;top:189px;width:77px;height:78px;background:var(--stone)"></div>
  <div class="tile" role="img" aria-label="Photo tile: lakeshore road in muted sand tones" style="left:207px;top:272px;width:237px;height:58px;background:linear-gradient(90deg,#a99c6a,#bcb28c)"></div>
  <div class="brand">BREVANI</div>
  <h1 class="title">Board of<br>Directors</h1>
  <p class="date">May 2024</p>
</section>

<!-- Mosaic, dark -->
<section class="slide slide--dark mosaic col-right row-3">
  <div class="tile" role="img" aria-label="Photo tile: dark pine forest" style="left:207px;top:8px;width:77px;height:76px;background:linear-gradient(#2e3a2c,#3a4630)"></div>
  <div class="tile" role="img" aria-label="Photo tile: golden forest canopy" style="left:207px;top:88px;width:77px;height:76px;background:linear-gradient(#8d7d4f,#6f6640)"></div>
  <div class="tile" role="img" aria-label="Photo tile: forest with winding road" style="left:207px;top:169px;width:77px;height:98px;background:linear-gradient(#4a5a2a,#6a7a3a)"></div>
  <div class="tile" role="img" aria-label="Photo tile: road winding beside a turquoise lake" style="left:287px;top:8px;width:76px;height:259px;background:linear-gradient(#4a5a2a,#5d7a3a 55%,#7fcfc0)"></div>
  <div class="tile" role="img" aria-label="Photo tile: pale lake water" style="left:367px;top:8px;width:77px;height:97px;background:linear-gradient(#eef6f4,#cfeae5)"></div>
  <div class="tile" style="left:367px;top:109px;width:77px;height:76px;background:#b9e3dc"></div>
  <div class="tile" style="left:367px;top:189px;width:77px;height:78px;background:var(--sand)"></div>
  <div class="tile" role="img" aria-label="Photo tile: lakeshore road with yellow trees" style="left:207px;top:272px;width:237px;height:58px;background:linear-gradient(90deg,#a9a34a,#9fd3c8)"></div>
  <div class="brand">BREVANI</div>
  <h1 class="title">Board of<br>Directors</h1>
  <p class="date">May 2024</p>
</section>

<!-- Panorama arc, light -->
<section class="slide slide--light pano col-left row-4">
  <svg class="art" viewBox="0 0 450 338">
    <defs>
      <linearGradient id="lakeA" x1="0" y1="0" x2="0" y2="1">
        <stop offset="0" stop-color="#b9d3ea"/><stop offset="0.3" stop-color="#7a8090"/>
        <stop offset="0.45" stop-color="#8a6a2a"/><stop offset="0.65" stop-color="#3c4a5a"/>
        <stop offset="1" stop-color="#6a7a4a"/>
      </linearGradient>
    </defs>
    <rect role="img" aria-label="Photo: snowy alpine peaks reflected in a mountain lake with autumn meadows" width="450" height="240" fill="url(#lakeA)"/>
    <path d="M0,220 Q225,172 450,220 V338 H0Z" fill="var(--arc-blue)"/>
    <path d="M0,232 Q225,184 450,232 V338 H0Z" fill="var(--arc-light)"/>
    <path d="M0,236 Q225,190 450,236 V338 H0Z" fill="#ffffff"/>
  </svg>
  <h1 class="title">Board of Directors</h1>
  <p class="date">May 2024</p>
  <div class="brand">BREVANI</div>
</section>

<!-- Panorama arc, dark -->
<section class="slide slide--dark pano col-right row-4">
  <svg class="art" viewBox="0 0 450 338">
    <rect role="img" aria-label="Photo: snowy alpine peaks reflected in a mountain lake with autumn meadows" width="450" height="240" fill="url(#lakeA)"/>
    <path d="M0,220 Q225,172 450,220 V338 H0Z" fill="var(--arc-light)"/>
    <path d="M0,224 Q225,178 450,224 V338 H0Z" fill="var(--arc-blue)"/>
    <path d="M0,236 Q225,190 450,236 V338 H0Z" fill="var(--navy)"/>
  </svg>
  <h1 class="title">Board of Directors</h1>
  <p class="date">May 2024</p>
  <div class="brand">BREVANI</div>
</section>

<!-- Panorama arc (wider crop), light -->
<section class="slide slide--light pano col-left row-5">
  <svg class="art" viewBox="0 0 450 338">
    <defs>
      <linearGradient id="lakeB" x1="0" y1="0" x2="0" y2="1">
        <stop offset="0" stop-color="#a9c8e6"/><stop offset="0.3" stop-color="#7a8296"/>
        <stop offset="0.45" stop-color="#7a6a2a"/><stop offset="0.7" stop-color="#4a5e7a"/>
        <stop offset="1" stop-color="#7a7a3a"/>
      </linearGradient>
    </defs>
    <rect role="img" aria-label="Photo: alpine peaks and lake with grassy shoreline" width="450" height="250" fill="url(#lakeB)"/>
    <path d="M0,228 Q225,200 450,244 V338 H0Z" fill="var(--arc-blue)"/>
    <path d="M0,240 Q225,212 450,252 V338 H0Z" fill="var(--arc-light)"/>
    <path d="M0,244 Q225,218 450,256 V338 H0Z" fill="#ffffff"/>
  </svg>
  <h1 class="title" style="top:261px">Board of Directors</h1>
  <p class="date" style="top:295px">May 2024</p>
  <div class="brand" style="left:300px;top:268px">BREVANI</div>
</section>

<!-- Panorama arc (wider crop), dark -->
<section class="slide slide--dark pano col-right row-5">
  <svg class="art" viewBox="0 0 450 338">
    <rect role="img" aria-label="Photo: alpine peaks and lake with grassy shoreline" width="450" height="250" fill="url(#lakeB)"/>
    <path d="M0,228 Q225,200 450,244 V338 H0Z" fill="var(--arc-light)"/>
    <path d="M0,232 Q225,205 450,247 V338 H0Z" fill="var(--arc-blue)"/>
    <path d="M0,244 Q225,218 450,256 V338 H0Z" fill="var(--navy)"/>
  </svg>
  <h1 class="title" style="top:261px">Board of Directors</h1>
  <p class="date" style="top:295px">May 2024</p>
  <div class="brand" style="left:300px;top:268px">BREVANI</div>
</section>

</body>
</html>
```